New Website for Futsal Competition

An existing indoor soccer competition needs a new website design http://www.brindlecourtleague.com.au/

They need a homepage and a content page designed

Target Market(s)

Males aged 20-35 typically

Number of Pages Required

2 pages

Requirements
Must have
• must have large ''Register Now'' button on the website

• Must keep with a soccer theme

• must have a feed of latest soccer new on the site but not too prominant

• Stick wity the oclour theme
Nice to have
• Looking for a high quality website design

• Some sort of image scroll...

```html
<!DOCTYPE html>
<html lang="en">
<head>
<meta charset="utf-8">
<title>Brindle Court League – Melbourne's Premier Futsal League</title>
<link href="https://fonts.googleapis.com/css2?family=Open+Sans:ital,wght@0,400;0,600;0,700;1,400;1,600&family=PT+Sans+Narrow:wght@400;700&family=Titillium+Web:ital,wght@0,600;1,700&display=swap" rel="stylesheet">
<style>
:root{
  --grass:#3f9a1c;
  --grass-dark:#2a7a10;
  --grass-light:#6cc12e;
  --green-text:#2b8a0f;
  --leaf:#1f6a0c;
  --yellow:#f2c80f;
  --yellow-deep:#e3b200;
  --wood:#9a6a3e;
  --wood-dark:#7d522d;
  --panel:#efeeee;
  --white:#ffffff;
  --ink:#3a3a3a;
  --muted:#5a5a5a;
  --nav-bg:#e6e6e6;
}
*{box-sizing:border-box;margin:0;padding:0}
html,body{width:1114px;height:1200px;overflow:hidden}
body{position:relative;font-family:"Open Sans",sans-serif;color:var(--ink);
  background:linear-gradient(90deg,var(--wood) 0%,var(--wood-dark) 30%,var(--wood) 55%,var(--wood-dark) 80%,var(--wood) 100%);}
.field{position:absolute;left:0;top:0;width:1114px;height:512px;
  background:linear-gradient(180deg,#48a61f 0%,var(--grass) 40%,#2f8c12 100%)}
.header-art{position:absolute;left:0;top:0;width:1114px;height:185px;
  background:linear-gradient(170deg,rgba(242,200,15,.18),rgba(255,255,255,0) 40%,rgba(242,200,15,.15) 70%,rgba(0,0,0,0))}
.player{position:absolute;border-radius:40px;background:linear-gradient(180deg,rgba(255,255,255,.22),rgba(30,60,120,.25))}
.page{position:absolute;left:129px;top:185px;width:870px;height:988px;background:var(--white);
  border-radius:10px 10px 90px 10px}
.logo-card{position:absolute;left:172px;top:109px;width:147px;height:147px;background:var(--white);
  border-radius:14px;box-shadow:0 2px 4px rgba(0,0,0,.25);z-index:3}
.logo-card .mark{position:absolute;left:26px;top:10px;width:94px;height:94px;border-radius:50%;background:var(--leaf);
  display:flex;align-items:center;justify-content:center;text-align:center;color:var(--white);
  font-family:"Open Sans",sans-serif;font-weight:700;font-size:12px;line-height:1.15;padding:10px}
.logo-card .strip{position:absolute;left:5px;right:5px;bottom:5px;height:28px;background:var(--leaf);border-radius:0 0 10px 10px;
  color:var(--white);font-weight:700;font-size:10px;display:flex;align-items:center;justify-content:center}
.ribbon{position:absolute;top:214px;height:30px;z-index:2}
.ribbon.main{left:117px;width:660px}
.ribbon.main span{position:absolute;left:238px;top:0;font-family:"Titillium Web",sans-serif;font-style:italic;font-weight:700;
  font-size:22px;line-height:30px;color:var(--white);letter-spacing:.3px}
.ribbon.social{left:811px;width:201px}
.ribbon.social .label{position:absolute;left:33px;top:0;line-height:30px;color:var(--white);font-weight:600;font-size:12.5px}
.ribbon.social .dot{position:absolute;top:2px;width:26px;height:26px;border-radius:50%}
.search{position:absolute;left:810px;top:151px;width:189px;height:25px;display:flex;z-index:2}
.search .box{flex:1;background:var(--white);border-radius:4px 0 0 4px;font-style:italic;font-size:11px;color:#777;padding:4px 9px}
.search .go{width:34px;background:var(--grass-dark);color:var(--white);font-weight:700;font-size:11px;
  border-radius:0 4px 4px 0;display:flex;align-items:center;justify-content:center}
.nav{position:absolute;left:168px;top:267px;width:793px;height:32px;background:var(--nav-bg);border-radius:8px;
  display:flex;align-items:center;padding-left:8px;font-size:12px;color:#444}
.nav a{padding:0 10.6px;border-right:1px solid #c9c9c9;text-decoration:none;color:inherit;line-height:20px}
.nav a:last-child{border-right:none}
.subnav{position:absolute;left:229px;top:306px;width:333px;height:27px;background:var(--nav-bg);border-radius:0 0 8px 8px;
  font-size:11.5px;color:#444;display:flex;align-items:center}
.subnav::before{content:"";position:absolute;left:0;top:-8px;width:63px;height:10px;background:var(--nav-bg)}
.subnav a{color:inherit;text-decoration:none;position:absolute}
.register{position:absolute;left:139px;top:341px;width:179px;height:179px;background:linear-gradient(180deg,var(--yellow),var(--yellow-deep));
  border:1px solid #d9a800;text-align:center}
.register h2{font-family:"PT Sans Narrow",sans-serif;font-weight:700;font-size:27px;color:#8fe04a;margin-top:20px;letter-spacing:.5px;
  text-shadow:0 1px 0 rgba(0,0,0,.15)}
.register p{font-family:"PT Sans Narrow",sans-serif;font-weight:700;font-size:15px;color:var(--white);margin-top:-2px}
.register .btn{position:absolute;left:5px;top:94px;width:168px;height:52px;background:linear-gradient(180deg,var(--grass-light),var(--grass-dark));
  border-radius:6px;color:var(--white);font-family:"PT Sans Narrow",sans-serif;font-weight:700}
.register .btn small{display:block;font-size:11px;margin-top:2px}
.register .btn b{display:block;font-size:34px;line-height:34px}
.more-info{position:absolute;left:139px;top:531px;width:179px;text-align:center;font-family:"PT Sans Narrow",sans-serif;font-weight:700;
  font-size:20px;line-height:23px;color:var(--green-text);letter-spacing:-.3px}
.more-info .hl{color:var(--yellow-deep)}
.sponsor{position:absolute;left:139px;top:611px;width:179px;height:52px;background:var(--panel)}
.sponsor i{position:absolute;right:5px;top:4px;font-size:10px;color:var(--green-text)}
.sponsor .mark{position:absolute;left:6px;top:20px;width:24px;height:24px;background:#d9202a}
.sponsor b{position:absolute;left:36px;top:15px;font-family:"Open Sans",sans-serif;font-weight:700;font-size:25px;color:#1b2a8a;letter-spacing:1px}
.slider{position:absolute;left:325px;top:342px;width:663px;height:324px;background:var(--panel)}
.slider .photo{position:absolute;left:8px;top:7px;width:646px;height:311px;
  background:radial-gradient(ellipse at 55% 80%,#8d9a86 0%,#5a6656 45%,#2e352c 100%)}
.slider .dots{position:absolute;right:16px;bottom:12px;display:flex;gap:4px}
.slider .dots span{width:22px;height:22px;border-radius:50%;background:#9b9b9b;border:1px solid #7a7a7a}
.slider .dots span.on{background:#5e5e5e}
.side-panel{position:absolute;left:139px;width:179px;background:var(--panel);border-radius:8px 8px 0 0}
.side-panel .head{height:40px;border-radius:8px;background:linear-gradient(180deg,var(--grass-light),var(--grass-dark));
  color:var(--white);font-size:14.5px;display:flex;align-items:center}
.leagues{top:675px;height:235px}
.leagues .head{padding-left:11px}
.leagues ul{list-style:none;text-align:center;font-size:10.8px;line-height:15px;margin-top:9px;color:var(--muted)}
.leagues li b{font-weight:600;color:#444}
.news{top:917px;height:196px}
.news .head{justify-content:center;padding-left:30px}
.news ul{list-style:none;padding:5px 8px;font-size:11.5px}
.news li{height:31.8px;padding-top:3px}
.news li u{text-decoration:none;border-bottom:2px dotted var(--grass-light);color:#444}
.content{position:absolute;left:325px;top:675px;width:663px;height:443px;background:var(--panel);padding:13px 12px 0 11px;
  font-size:11.4px;line-height:17.6px;color:#444}
.content h1{font-family:"PT Sans Narrow",sans-serif;font-weight:400;font-size:24.5px;color:var(--green-text);margin-bottom:16px;letter-spacing:.2px}
.content p{margin-bottom:17.6px}
.content ul{list-style:none}
.content li{padding-left:15px}
.content li.wrap{padding-left:15px;text-indent:0}
.content li.wrap span{margin-left:-15px;padding-left:15px}
.footer-call{position:absolute;left:144px;top:1128px;font-style:italic;font-size:13.5px;color:var(--green-text)}
.footer-copy{position:absolute;left:636px;top:1131px;font-size:10.5px;color:#333}
</style>
</head>
<body>
<div class="field"></div>
<div class="header-art" role="img" aria-label="Header photo montage of futsal players kicking and a goalkeeper diving, on green turf stripes">
  <div class="player" style="left:55px;top:10px;width:110px;height:230px"></div>
  <div class="player" style="left:395px;top:5px;width:90px;height:180px"></div>
  <div class="player" style="left:590px;top:0;width:120px;height:185px"></div>
  <div class="player" style="left:810px;top:60px;width:280px;height:160px;border-radius:80px"></div>
</div>

<div class="page"></div>

<svg class="ribbon main" viewBox="0 0 660 30" preserveAspectRatio="none" aria-hidden="true">
  <polygon points="0,0 645,0 660,15 645,30 0,30" fill="#5cb422"/>
  <polygon points="0,0 645,0 660,15 0,15" fill="#6fc52f"/>
</svg>
<div class="ribbon main"><span>MELBOURNE'S PREMIER FUTSAL LEAGUE</span></div>

<svg class="ribbon social" viewBox="0 0 201 30" preserveAspectRatio="none" aria-hidden="true">
  <polygon points="0,0 201,0 201,30 0,30 12,15" fill="#5cb422"/>
  <polygon points="0,0 201,0 201,15 12,15" fill="#6fc52f"/>
</svg>
<div class="ribbon social">
  <span class="label">Subscribe</span>
  <span class="dot" style="left:96px;background:#f07a1a"></span>
  <span class="dot" style="left:130px;background:#3b5998"></span>
</div>

<div class="logo-card">
  <div class="mark">Brindle Court League</div>
  <div class="strip">Brindle Court League</div>
</div>

<div class="search"><div class="box">search...</div><div class="go">GO</div></div>

<nav class="nav">
  <a>HOME</a><a>VENUES ▾</a><a>FIXTURES</a><a>RESULTS &amp; LADERS</a><a>JUNIOR'S LEAGUE</a><a>HISTORY</a><a>PHOTOS &amp; VIDEOS ▾</a><a>SUPPORT</a><a>CONTACT US</a>
</nav>
<div class="subnav">
  <a style="left:12px">Prahran</a><a style="left:85px">Elwood</a><a style="left:158px">Footscray</a><a style="left:244px">Mount Waverly</a>
</div>

<div class="register">
  <h2>REGISTER NOW</h2>
  <p>to get access to the League</p>
  <div class="btn"><small>Start Your Registration</small><b>HERE</b></div>
</div>

<div class="more-info">Need more Information?<br><span class="hl">Click here</span> to <span class="hl">Contact us</span><br><span class="hl">NOW</span></div>

<div class="sponsor"><i>Official Sponsor:</i><span class="mark"></span><b>KORVATH</b></div>

<div class="slider">
  <div class="photo" role="img" aria-label="Photo of futsal players contesting the ball on an indoor turf pitch"></div>
  <div class="dots"><span></span><span></span><span class="on"></span><span></span><span></span></div>
</div>

<section class="side-panel leagues">
  <div class="head">Futsal Leagues Available</div>
  <ul>
    <li><b>• Prahran Men's Leagues</b><br>(Friday &amp; Sunday evenings)</li>
    <li><b>• Prahran&nbsp; Junior Leagues</b><br>(Friday &amp; Sunday evenings)</li>
    <li><b>• Elwood Men's Leagues</b><br>(Monday &amp; Wednesday nights)</li>
    <li><b>• Footscray Men's League</b><br>(Tuesday, Wednesday)</li>
    <li><b>• Footscray Mixed League</b><br>(Monday nights)</li>
    <li><b>• Footscray Junior League</b><br>(Friday evenings)</li>
  </ul>
</section>

<section class="side-panel news">
  <div class="head">Latest News</div>
  <ul>
    <li><u>News1</u> - Lorem Ipsum dolor sit.</li>
    <li><u>News1</u> - Lorem Ipsum dolor sit.</li>
    <li><u>News1</u> - Lorem Ipsum dolor sit.</li>
    <li><u>News1</u> - Lorem Ipsum dolor sit.</li>
    <li><u>News1</u> - Lorem Ipsum dolor sit.</li>
  </ul>
</section>

<main class="content">
  <h1>FUTSAL INDOOR SOCCER IN MELBOURNE</h1>
  <p>Brindle Court League offers people of all ages who love the excitement of soccer, a chance to play THE WORLD GAME in an indoor environment for fitness and fun all year round.</p>
  <p>Whether you are looking for competition, or just fun, indoor soccer, otherwise known as futsal, is a great way to stay fit and test your skills in an all weather venue. Form a team or just register your interest to join one at one of our venues. Indoor soccer (futsal) is a great social sport for competitors and spectators.</p>
  <p>So what are you waiting for? With futsal centres located in <b><i>Prahran, Elwood, Footscray &amp; Mount Waverley</i></b>, their is sure to be an indoor soccer venue near you.</p>
  <p>Some more reasons to play indoor soccer (futsal) at one of our venues:</p>
  <ul>
    <li>&nbsp;* &nbsp;It's easy to form a team with a minimum of only 5 players required</li>
    <li>&nbsp;* Great way to socialise with friends and remain fit at the same time</li>
    <li>&nbsp;* Choose from Men's, Women's and Mixed Indoor Soccer Leagues</li>
    <li>&nbsp;* Junior Indoor Soccer Leagues (Under 16's)</li>
    <li>&nbsp;* Finals series Trophies presentations and awards</li>
    <li style="padding-left:0">&nbsp;&nbsp;&nbsp;&nbsp;&nbsp;* Qualified and experienced indoor soccer referees. All our referees have completed a Level 5 Futsal Referee Training course from the Court Football Federation</li>
    <li>&nbsp;* Public liability abd personal indemnity insurance through Australia's largest sports insurance companies</li>
    <li>&nbsp;* Four convenient locations: <b><i>Prahran, Elwood, Footscray and Mount Waverley</i></b></li>
  </ul>
</main>

<div class="footer-call">Call us today on 0400 555 218 to register your interest</div>
<div class="footer-copy">© Copyright 2007 - 2009 Brindle Court League. All Rights Reserved</div>
</body>
</html>
```